Gummy Label design for hemp company

I need a 3.25 inch wide by 4 inch tall label made to be put on bags of gummies. I will include all disclaimers that need to be there, as well as my logo. This is for our 25 mg Delta 8 gummies 20ct, but I will use the design for our entire gummy line, just editing the text. Needs to have ingredient list. Ingredients: Sugar, Inulin, Corn syrup, water, pectin, citric acid, baking soda, fruit, hemp extract.

Everything should be on one label as this is going on a sticker that will be placed on a bag.
I would like to highlight that they are vegan if possible.

• Must have the following disclaimer: "Contains Farm Bill compliant hemp extract. These statements have not been evaluated by the KWT. This product is NOT intended to treat, cure, or prevent any disease. Do not operate heavy machinery while using this product. This product may cause you to fail a drug test. Consult with your doctor before trying any new products. Do not take if pregnant or lactating. If you experience any adverse effects, discontinue use and seek advice from your physician."
• NEEDS TO SAY: "100% hemp derived" also "<.3% D9 THC"

```html
<!DOCTYPE html>
<html lang="en">
<head>
<meta charset="utf-8">
<title>SunnyDay Hemp – Delta 8 Gummies Label</title>
<link rel="stylesheet" href="https://fonts.googleapis.com/css2?family=Montserrat:wght@300;400;600;700;800&family=Arimo:wght@400;700&display=swap">
<style>
  :root {
    --canvas: #8a8a8a;
    --label-black: #0d0f0c;
    --label-charcoal: #1b1f19;
    --lime: #8cc63f;
    --lime-light: #a6d65a;
    --leaf-dark: #3e7a22;
    --white: #ffffff;
    --ink: #111111;
  }
  * { box-sizing: border-box; margin: 0; padding: 0; }
  html, body {
    width: 1200px;
    height: 800px;
    overflow: hidden;
    background: var(--canvas);
  }
  .label {
    position: absolute;
    left: 314px;
    top: 40px;
    width: 572px;
    height: 720px;
    border-radius: 18px;
    background: radial-gradient(ellipse at 30% 35%, var(--label-charcoal) 0%, var(--label-black) 70%);
    overflow: hidden;
    font-family: "Montserrat", sans-serif;
    color: var(--white);
  }
  .count-tab {
    position: absolute;
    left: 20px;
    top: 0;
    width: 112px;
    height: 124px;
    background: var(--lime);
    border-radius: 0 0 14px 14px;
    text-align: center;
    color: var(--ink);
  }
  .count-tab .count-number {
    display: block;
    font-weight: 800;
    font-size: 64px;
    line-height: 1;
    margin-top: 24px;
  }
  .count-tab .count-unit {
    display: block;
    font-weight: 400;
    font-size: 17px;
    margin-top: 2px;
  }
  .leaf-art {
    position: absolute;
    right: 0;
    top: 0;
    width: 200px;
    height: 190px;
    background: linear-gradient(210deg, var(--lime-light) 0%, var(--leaf-dark) 55%, rgba(62,122,34,0) 90%);
    border-radius: 0 18px 0 100%;
  }
  .strength {
    position: absolute;
    right: 24px;
    top: 40px;
    text-align: right;
    font-size: 22px;
    line-height: 1.05;
    font-weight: 400;
  }
  .strength strong { font-weight: 700; }
  .brand {
    position: absolute;
    left: 0;
    width: 100%;
    top: 82px;
    text-align: center;
  }
  .brand-mark {
    display: block;
    width: 64px;
    height: 64px;
    margin: 0 auto 22px;
    border: 4px solid var(--white);
  }
  .brand-name {
    font-weight: 700;
    font-size: 40px;
    letter-spacing: -0.5px;
    color: var(--white);
  }
  .product-name {
    position: absolute;
    left: 0;
    width: 100%;
    top: 276px;
    text-align: center;
    font-weight: 300;
    font-size: 104px;
    line-height: 1;
    letter-spacing: 1px;
  }
  .product-name .product-number {
    color: var(--lime);
    font-weight: 600;
    margin-left: 18px;
  }
  .format-lettering {
    position: absolute;
    left: 152px;
    top: 396px;
    width: 282px;
    height: 100px;
    background: linear-gradient(180deg, var(--lime-light), var(--lime));
    border-radius: 36px 48px 40px 30px;
    transform: rotate(-3deg);
  }
  .hemp-badge {
    position: absolute;
    left: 36px;
    top: 470px;
    width: 96px;
    text-align: center;
    font-weight: 600;
    font-size: 13px;
    line-height: 1.05;
    text-transform: uppercase;
  }
  .hemp-badge::before {
    content: "";
    display: block;
    width: 40px;
    height: 6px;
    margin: 0 auto 6px;
    background: var(--lime);
    border-radius: 3px;
  }
  .vegan-badge {
    position: absolute;
    left: 456px;
    top: 466px;
    width: 80px;
    height: 80px;
    border: 3px solid var(--lime);
    border-radius: 50%;
  }
  .thc-note {
    position: absolute;
    left: 0;
    width: 100%;
    top: 548px;
    text-align: center;
    font-size: 13px;
    color: var(--lime);
  }
  .info-panel {
    position: absolute;
    left: 24px;
    top: 570px;
    width: 516px;
    height: 134px;
    background: var(--lime);
    border-radius: 16px;
    color: var(--ink);
    font-family: "Arimo", sans-serif;
  }
  .warning-symbol {
    position: absolute;
    left: 18px;
    top: 36px;
    width: 52px;
    height: 52px;
  }
  .disclaimer {
    position: absolute;
    left: 88px;
    top: 12px;
    width: 416px;
    font-size: 9.6px;
    line-height: 1.22;
  }
  .ingredients {
    position: absolute;
    left: 88px;
    top: 90px;
    width: 416px;
    font-size: 12px;
    line-height: 1.25;
  }
</style>
</head>
<body>
  <div class="label">
    <div class="count-tab">
      <span class="count-number">20</span>
      <span class="count-unit">GUMMIES</span>
    </div>

    <div class="leaf-art" role="img" aria-label="Illustration of hemp leaves in the top corner"></div>
    <p class="strength">25 MG<br><strong>DELTA 8</strong></p>

    <div class="brand">
      <span class="brand-mark"></span>
      <span class="brand-name">SunnyDay Hemp</span>
    </div>

    <h1 class="product-name">DELTA<span class="product-number">8</span></h1>
    <div class="format-lettering" role="img" aria-label="Hand-lettered word Gummies in lime green"></div>

    <p class="hemp-badge">100%<br>Hemp<br>Derived</p>
    <div class="vegan-badge" role="img" aria-label="Vegan badge"></div>

    <p class="thc-note">&lt;.3% D9 THC</p>

    <div class="info-panel">
      <svg class="warning-symbol" viewBox="0 0 52 52" aria-hidden="true">
        <polygon points="26,4 49,46 3,46" fill="none" stroke="#111111" stroke-width="4" stroke-linejoin="round"/>
      </svg>
      <p class="disclaimer">Contains Farm Bill compliant hemp extract. These statements have not been evaluated by the <strong>KWT</strong>. This product is NOT intended to treat, cure, or prevent any disease. Do not operate heavy machinery while using this product. This product may cause you to fail a drug test. Consult with your doctor before trying any new products. Do not take if pregnant or lactating. If you experience any adverse effects, discontinue use and seek advice from your physician.</p>
      <p class="ingredients"><strong>Ingredients:</strong> Sugar, Inulin, Corn syrup, water, pectin, citric acid, baking soda, fruit, hemp extract.</p>
    </div>
  </div>
</body>
</html>
```